| ■お仕事内容 海外の高級ファッションブランドを販売するサイト用の無償修理保証のバナー製作をお願いいたします。 メンズ、レディースどちらも取り扱っているブランドのため、どちらでも使えるデザインが望ましいです。 ■バナーに記載する内容 「1年間無償修理保証」ということが伝わる文章を入れてください。 ※独自のサービスのため、「当店だけの・・・」など独自の付加価値サービスである文言を入れたいです。 ■重視する点 ・高級感のあるデザイン(ごちゃごちゃしていない、シンプルで目を引くもの) ・フラットデザインが基調になっているサイトにマッチするデザイン ・ファッション系のサイトに合うデザイン ・本物である安心感・信頼感のあるデザイン ■報酬 5,000円 ■応募条件 WEBサイトのバナー、アイコンなどの製作経験をお持ちの方 ご提案価格と実績のバランスを見てお仕事をお願いする方を選定させていただきます。 たくさんのご応募お待ちしております。 何卒宜しくお願いいたします。 |

```html
<!DOCTYPE html>
<html lang="ja">
<head>
<meta charset="UTF-8">
<title>1年間無償修理保証</title>
<link rel="stylesheet" href="https://fonts.googleapis.com/css2?family=Noto+Sans+JP:wght@500&family=Noto+Serif+JP:wght@400;500&display=swap">
<style>
  :root {
    --gold: #9c8a3a;
    --gold-line: #b8a654;
    --ink: #2e2e2e;
    --paper: #ffffff;
    --frame: #d6d6d6;
  }
  html, body {
    margin: 0;
    padding: 0;
    overflow: hidden;
    background: var(--paper);
  }
  .banner {
    position: relative;
    width: 1200px;
    height: 188px;
    box-sizing: border-box;
    border: 2px solid var(--frame);
    background: var(--paper);
    overflow: hidden;
  }
  .ribbon {
    position: absolute;
    left: 26px;
    top: -2px;
    width: 186px;
    height: 178px;
  }
  .ribbon-label {
    position: absolute;
    left: 26px;
    top: 12px;
    width: 186px;
    margin: 0;
    text-align: center;
    font-family: "Noto Sans JP", sans-serif;
    font-weight: 500;
    font-size: 44px;
    line-height: 62px;
    letter-spacing: 2px;
    color: var(--paper);
  }
  .headline {
    position: absolute;
    left: 246px;
    top: 34px;
    margin: 0;
    font-family: "Noto Serif JP", serif;
    font-weight: 500;
    font-size: 80px;
    line-height: 96px;
    letter-spacing: 27px;
    color: var(--ink);
    white-space: nowrap;
  }
  .headline .accent {
    color: var(--gold);
  }
  .underline {
    position: absolute;
    left: 250px;
    top: 142px;
    width: 926px;
    height: 2px;
    background: var(--gold-line);
  }
</style>
</head>
<body>
  <div class="banner">
    <svg class="ribbon" viewBox="0 0 186 178" aria-hidden="true">
      <polygon points="0,0 186,0 186,178 93,160 0,178" fill="var(--gold)"/>
    </svg>
    <p class="ribbon-label">当店<br>限定</p>
    <h1 class="headline">1年間<span class="accent">無償</span>修理保証</h1>
    <div class="underline"></div>
  </div>
</body>
</html>
```